Cool blackchain based app company needs a website :)

pillcheckhub.net

Kinda says it all!! This is an app which sits on your smartfone / tablet. You scan a QR code from a medicinal product and our app will verify if the product you have is genuine. It's simple, It's free.

The design could be very modern and simple. It should show in graphical form how the app works and have FAQ's etc.

pillcheckhub.net is designed specifically to allow consumers verify that the medical products which they have purchased are genuine.

Detailed brief with content attached. Logo in high res and QR code attached.

Full website required.
Updates

Target Market(s)

Pharmaceutical

Industry/Entity Type

Pharmaceutical

Coding

Coded - Design and coding required

Number of Pages Required

3 page

Colors

Designer to choose colors to be used in the design.

Requirements
Must have
• Strong visuals - very simple navigation - 3 pages
Nice to have
• Animation of the process
Should not have
• Jargon!

```html
<!DOCTYPE html>
<html lang="en">
<head>
<meta charset="utf-8">
<title>pillcheckhub.net</title>
<link rel="stylesheet" href="https://fonts.googleapis.com/css2?family=Ubuntu:wght@400;500;700&family=Open+Sans:wght@400;600;700&display=swap">
<style>
:root{
  --green:#5aa12b;
  --green-dark:#4a8b22;
  --navy:#1c3b6b;
  --ink:#333a44;
  --muted:#555d66;
  --icon-blue:#23a3e6;
  --white:#ffffff;
  --page:#ffffff;
  --hero-bg:#f5f6f7;
}
*{margin:0;padding:0;box-sizing:border-box}
html,body{width:1200px;height:4688px;overflow:hidden;background:var(--page)}
body{font-family:"Open Sans",Arial,sans-serif;color:var(--ink);position:relative}
.section{position:absolute;left:0;width:1200px}

/* header + hero */
.hero{top:0;height:610px;background:var(--hero-bg)}
.brand{position:absolute;display:flex;align-items:center;gap:10px;font-family:"Ubuntu",sans-serif;font-weight:700;color:var(--navy)}
.brand-dot{width:26px;height:26px;border-radius:50%;background:var(--green)}
.hero .brand{left:194px;top:52px;font-size:22px}
.main-nav{position:absolute;top:66px;right:156px;display:flex;gap:86px;font-family:"Ubuntu",sans-serif;font-size:15px;font-weight:500;color:var(--ink)}
.main-nav .active{border-bottom:2px solid var(--ink);padding-bottom:4px}
.slide-dots{position:absolute;left:28px;top:310px;display:flex;flex-direction:column;gap:16px}
.slide-dots span{width:10px;height:10px;border-radius:50%;background:#c9ccd0}
.slide-dots span.on{background:var(--green)}
.hero-copy{position:absolute;left:156px;top:278px;width:520px}
.hero-title{font-family:"Ubuntu",sans-serif;font-weight:500;font-size:29px;line-height:1.3;color:var(--navy)}
.hero-title em{font-style:normal;color:var(--green)}
.hero-sub{margin-top:14px;font-size:12px;font-weight:700;color:var(--ink)}
.btn{position:absolute;left:156px;top:440px;width:248px;height:50px;border-radius:25px;background:var(--green);color:var(--white);font-family:"Ubuntu",sans-serif;font-weight:500;font-size:14px;display:flex;align-items:center;justify-content:center;letter-spacing:.5px}
.hero-art{position:absolute;left:650px;top:60px;width:440px;height:540px;border-radius:50% 50% 20px 20px;background:radial-gradient(circle at 50% 35%,#9fd8f0 0%,#c8ead2 45%,rgba(245,246,247,0) 72%)}

/* photo bands */
.band{display:flex;flex-direction:column;align-items:center;justify-content:center;color:var(--white)}
.band-title{font-family:"Ubuntu",sans-serif;font-weight:700;font-size:40px;text-shadow:0 2px 8px rgba(0,0,0,.35)}
.band-icon{margin-top:22px}
.scan{top:610px;height:468px;background:linear-gradient(135deg,#3a2a22 0%,#6f5a4b 40%,#8c8a86 70%,#4a4c52 100%)}
.scan p{font-family:"Ubuntu",sans-serif;font-size:24px;line-height:1.6;text-align:center;text-shadow:0 2px 6px rgba(0,0,0,.5)}
.authenticity{top:1328px;height:469px;background:linear-gradient(120deg,#0d1e2c 0%,#2c4a62 45%,#4a6a82 70%,#1a2c3a 100%)}
.anonymity{top:2125px;height:469px;background:linear-gradient(100deg,#1e262e 0%,#3c4852 45%,#b7bec6 80%,#e4e7ea 100%)}
.security{top:2781px;height:469px;background:linear-gradient(110deg,#08152a 0%,#15305a 45%,#6c84a8 75%,#2a3a55 100%)}
.safety{top:3641px;height:469px;background:linear-gradient(120deg,#d6dde2 0%,#2d6a8e 30%,#0f4f78 60%,#dfe4e8 100%)}

/* text blocks */
.copy{display:flex;flex-direction:column;align-items:center;justify-content:center;text-align:center}
.copy p{width:900px;font-size:14.5px;line-height:1.65;color:var(--muted)}
.copy p+p{margin-top:18px}
.intro{top:1078px;height:250px}
.tagline{margin-top:22px;font-family:"Ubuntu",sans-serif;font-weight:700;font-size:30px;color:var(--green)}
.copy-auth{top:1797px;height:328px}
.copy-anon{top:2594px;height:187px}
.copy-sec{top:3250px;height:391px}
.copy-safe{top:4110px;height:343px}

/* footer */
.footer{top:4453px;height:235px;background:#f7f8f9;border-top:1px solid #e6e8ea}
.footer .brand{left:50%;transform:translateX(-50%);top:60px;font-size:18px}
.footer-nav{position:absolute;left:0;right:0;top:192px;display:flex;justify-content:center;gap:110px;font-family:"Ubuntu",sans-serif;font-size:13px;font-weight:500;color:var(--ink)}
</style>
</head>
<body>

<header class="section hero">
  <div class="brand"><span class="brand-dot"></span>pillcheckhub.net</div>
  <nav class="main-nav">
    <span class="active">HOME</span><span>ABOUT US</span><span>FAQ'S</span>
  </nav>
  <div class="slide-dots"><span class="on"></span><span></span><span></span><span></span></div>
  <div class="hero-copy">
    <h1 class="hero-title"><em>30% of all medicine</em> bought online is counterfeit Are you sure that the medication you take is genuine?</h1>
    <p class="hero-sub">Be Safe, Authenticate Protect your health with pillcheckhub</p>
  </div>
  <a class="btn">LEARN MORE</a>
  <div class="hero-art" role="img" aria-label="Illustration of a tree whose branches end in round medical icons: pills, syringe, hospital, ambulance, heart monitor"></div>
</header>

<section class="section band scan" role="img" aria-label="Photo of a hand holding a smartphone scanning a code">
  <p>Scan the pillcheckhub QR code which is printed on<br>your medication using your phone or tablet</p>
</section>

<section class="section copy intro">
  <p>Pillcheckhub will authenticate your medicine against the manufacturers own production records and<br>pillcheckhub will tell you immediately if your medicine is genuine</p>
  <div class="tagline">Its Quick, Its Secure, Its Free</div>
</section>

<section class="section band authenticity" role="img" aria-label="Photo of a scientist working at laboratory production equipment">
  <h2 class="band-title">Guaranteed Authenticity</h2>
  <svg class="band-icon" width="52" height="64" viewBox="0 0 52 64" fill="none" stroke="#23a3e6" stroke-width="2.5">
    <circle cx="26" cy="24" r="18"/><circle cx="26" cy="24" r="11"/>
    <path d="M15 38 L8 60 L17 55 L21 63 L26 43"/><path d="M37 38 L44 60 L35 55 L31 63 L26 43"/>
  </svg>
</section>

<section class="section copy copy-auth">
  <p>Pillcheckhub has a unique and highly secure Blockchain database which contains details of billions of batches of medicines manufactured across the world. Each time a manufacturer produces a batch of medicine, they send the details of that product to our secure Blockchain database. Our database records details of that batch of medicine and issues a unique encrypted QR code for every single batch. This code is printed on the medicine packet and it's packaging.</p>
  <p>You simply scan the QR code from your meds using your phone or tablet. The pillcheckhub app unencrypts this code, verifies it against the details provided by the manufacturer and confirms if the medication is genuine or not directly to you on your device.</p>
</section>

<section class="section band anonymity" role="img" aria-label="Photo of a doctor in a white coat holding a tablet">
  <h2 class="band-title">Guaranteed Anonymity</h2>
  <svg class="band-icon" width="44" height="56" viewBox="0 0 44 56" fill="none" stroke="#23a3e6" stroke-width="2.5">
    <rect x="4" y="4" width="36" height="48" rx="3"/>
    <path d="M11 16h22M11 24h22M11 32h22M11 40h14"/>
  </svg>
</section>

<section class="section copy copy-anon">
  <p>Pillcheckhub does NOT record any personal or health information You don't have to log on to<br>pillcheckhub and we don't ask you to register</p>
</section>

<section class="section band security" role="img" aria-label="Photo of hands presenting a glowing shield with a medical cross">
  <h2 class="band-title">Guaranteed Security</h2>
  <svg class="band-icon" width="48" height="56" viewBox="0 0 48 56" fill="none" stroke="#23a3e6" stroke-width="2.5">
    <path d="M24 3 L44 10 V26 C44 40 35 49 24 53 C13 49 4 40 4 26 V10 Z"/>
    <path d="M14 27 L21 34 L34 20"/>
  </svg>
</section>

<section class="section copy copy-sec">
  <p>Pillcheckhub are the first and only company in the world to use a (patent pending) encrypted specifically designed secure Blockchain database architecture for asset recording and authentication</p>
  <p>A Blockchain database is made up of a large network of independent database servers, each of which are in sync with each other. As soon as a record is appended to the database, all instances of the database simultaneously update Every record added to the database must contain encrypted keys before it is accepted by the Blockchain database.</p>
  <p>These keys form an interlinking chain This multitude of in-sync databases and verified chain data structure makes the pillcheckhub database impossible to hack</p>
</section>

<section class="section band safety" role="img" aria-label="Photo of a tablet screen showing a digital security interface">
  <h2 class="band-title">Guaranteed Safety</h2>
  <svg class="band-icon" width="70" height="70" viewBox="0 0 70 70" fill="none" stroke="#23a3e6" stroke-width="2.5">
    <circle cx="35" cy="35" r="31"/><circle cx="35" cy="35" r="22"/><circle cx="35" cy="35" r="13"/><circle cx="35" cy="35" r="4"/>
  </svg>
</section>

<section class="section copy copy-safe">
  <p>If you are taking medication you are doing so for a specific reason. It is imperative that your medication has been produced in accordance with strict international standards and that your medication contains the correct medicinal dosage The international pharmaceutical industry carefully manages their production processes to ensure the highest standards of product manufacture, production and distribution However, as in many industries, counterfeiting is a high value business.</p>
  <p>Counterfeit medicines cost the pharmaceutical industry more than €110 billion annually, €110 billion which otherwise would be invested into medical research and treatment development The financial cost is nothing compared to the loss of life. More than one million people's lives are lost each year due to counterfeit drugs. Counterfeit medicine often contains no active medicinal content or can contain a dangerous mix of ingredients. Whatever the mix, the medicine is not what it is claimed to be and the consequences of taking it can be lethal</p>
</section>

<footer class="section footer">
  <div class="brand"><span class="brand-dot"></span>pillcheckhub.net</div>
  <nav class="footer-nav"><span>HOME</span><span>ABOUT US</span><span>FAQ'S</span></nav>
</footer>

</body>
</html>
```